Flyer-Design für Babyfotograf
grinsi77 ist auf alle meine Wünsche eingegangen und hat das Layout sehr gut umgesetzt. Vielen Dank für die gute und reibungslose Zusammenarbeit.
Zielgruppe
Als Fotograf bin ich spezialisiert auf Babybauch- und Neugeborenenshootings, meine Zielgruppe sind daher schwangere Frauen und Familien die bald / vor kurzem Nachwuchs erwartet haben.
Neben den beiden sparten biete ich noch Baby- und Familienshootings an.
Aufgabenstellung
Ich hätte gerne einen besonderen Flyer, ein Faltspiel.
Die Lieferung der fertigen Datei bitte als offene Indesign 5.5 Datei, falls mal Änderungen anstehen und als druckfertige Datei im PDF Format.
Das Datenblatt der Druckerei finden Sie hier:
http://www.kammerl-satz.de/Papierwelt-Laden/PDF-Vorlagen/Vorlage_Endlosfaltkarte_DL.pdf
In der Anlage bekommen Sie einige Infos rund um meine Dienstleistungen, es wäre toll wenn diese textlich ggf. noch besser angepasst werden auf den Kundennutzen und die Vorteile welche der Kunde hat.
Ich hab mal noch einen Flyer beigefügt um mein corporate design zu erkennen.

```html
<!DOCTYPE html>
<html lang="de">
<head>
<meta charset="utf-8">
<title>Faltflyer Babyfotograf – Präsentation</title>
<link rel="stylesheet" href="https://fonts.googleapis.com/css2?family=Lobster&family=Bitter:wght@300;400;700&display=swap">
<style>
:root{
  --stage:#3d3d3d;
  --red:#8e2a1f;
  --beige:#e3dcd1;
  --beige-light:#eee9e1;
  --white:#ffffff;
  --ink:#4a4440;
  --band-red:#e20f14;
  --band-orange:#f29100;
}
*{margin:0;padding:0;box-sizing:border-box}
html,body{width:730px;height:1200px;overflow:hidden;background:var(--stage)}
.sheet{position:relative;width:730px;height:1200px;font-family:"Bitter",Georgia,serif;color:var(--ink)}
.thumb,.spread{position:absolute;overflow:hidden;background:var(--beige)}
.thumb{left:12px;width:160px;height:80px}
.spread{left:182px;width:532px;height:266px}
.row1{top:28px}.row2{top:319px}.row3{top:611px}.row4{top:903px}
.abs{position:absolute}
.photo{position:absolute}
.tone-wood{background:linear-gradient(160deg,#8a7f78,#b59d7a 55%,#c7a39a)}
.tone-warm{background:linear-gradient(150deg,#d9c7b3,#b08f78)}
.tone-dark{background:linear-gradient(150deg,#3c3f4a,#7a5e50)}
.tone-grey{background:linear-gradient(150deg,#5c5c5c,#bdbdbd)}
.tone-park{background:linear-gradient(170deg,#c9cdd0,#8a8f6f 60%,#6f6a5a)}
.tone-field{background:linear-gradient(170deg,#e6d7a8,#8e9a58 60%,#5f6b3a)}
.tone-soft{background:linear-gradient(150deg,#f1e7dc,#d4b8a3)}
.tone-blue{background:linear-gradient(150deg,#9aa6b0,#c8a88e)}
.script{font-family:"Lobster",cursive;color:var(--red);line-height:1}
.brand{position:absolute;border-radius:50%;background:var(--red);display:flex;align-items:center;justify-content:center;text-align:center}
.brand-name{font-family:"Bitter",Georgia,serif;font-weight:300;color:var(--white);letter-spacing:.12em;text-transform:uppercase}
.card{position:absolute;background:var(--white)}
.body-text{font-size:8.2px;line-height:1.38;font-weight:300}
.body-text b{font-weight:700}
.contact-title{font-weight:700;color:var(--red);font-size:8.4px;line-height:1.3}
.contact-list{list-style:none;font-size:5.8px;font-weight:300;margin-top:5px}
.contact-list li{display:flex;align-items:center;gap:4px;margin-bottom:3.4px}
.contact-list svg{width:7px;height:7px;flex:none;fill:var(--red)}
.reasons{font-size:5.4px;line-height:1.3;font-weight:300;overflow:hidden}
.reasons p{margin-bottom:2.4px}
.reasons .key{font-family:"Lobster",cursive;color:var(--red);font-size:6px}
.band{position:absolute;left:0;width:100%;display:flex;align-items:center;justify-content:center;font-size:3.2px;font-weight:700;color:#333;text-align:center}
.tiny{font-size:2.6px;line-height:1.3;font-weight:300}
</style>
</head>
<body>
<main class="sheet">

  <!-- Titelseite -->
  <section class="thumb row1" aria-label="Vorschau Titelseite">
    <div class="photo tone-wood" style="left:0;top:10px;width:108px;height:70px;clip-path:polygon(0 12%,100% 0,100% 100%,0 100%)" role="img" aria-label="Neugeborenes schlafend in einer Holzkiste"></div>
    <div class="script abs" style="left:3px;top:4px;font-size:7px">Es gibt Momente,</div>
    <div class="brand" style="left:92px;top:6px;width:46px;height:46px"><span class="brand-name" style="font-size:3px">Jonas Keller</span></div>
    <div class="script abs" style="left:118px;top:60px;font-size:5.6px">die kommen<br>nie wieder…</div>
  </section>

  <section class="spread row1" aria-label="Titelseite">
    <div class="photo tone-wood" style="left:0;top:0;width:400px;height:266px;clip-path:polygon(0 26%,86% 0,92% 100%,0 100%)" role="img" aria-label="Neugeborenes schlafend auf Fell in einer Holzkiste"></div>
    <h1 class="script abs" style="left:12px;top:14px;font-weight:400"><span style="font-size:21px">Es gibt </span><span style="font-size:33px">Momente,</span></h1>
    <div class="brand" style="left:311px;top:22px;width:170px;height:170px">
      <span class="brand-name" style="font-size:8.4px">Jonas Keller<br><span style="text-transform:none;letter-spacing:.1em;font-size:7px">babyfotos-kellerstudio.de</span></span>
    </div>
    <p class="script abs" style="left:372px;top:208px;font-size:23px;line-height:1.2">die kommen<br>nie wieder…</p>
  </section>

  <!-- Innenseite -->
  <section class="thumb row2" aria-label="Vorschau Innenseite">
    <div class="photo tone-park" style="left:0;top:0;width:40px;height:20px" role="img" aria-label="Schwangere im Park"></div>
    <div class="photo tone-dark" style="left:0;top:20px;width:40px;height:40px" role="img" aria-label="Schwangere mit Kind"></div>
    <div class="photo tone-warm" style="left:0;top:60px;width:40px;height:20px" role="img" aria-label="Baby mit Mütze"></div>
    <div class="script abs" style="left:48px;top:4px;font-size:5.4px;text-align:center;width:66px">… wie die ersten Lebenstage eures Babys!</div>
    <div class="photo tone-soft" style="left:43px;top:20px;width:37px;height:22px" role="img" aria-label="Neugeborenes auf Decke"></div>
    <div class="photo tone-field" style="left:80px;top:20px;width:37px;height:22px" role="img" aria-label="Paar auf Wiese"></div>
    <div class="card tiny" style="left:44px;top:44px;width:72px;height:34px;padding:4px">Zarte Momente mit Euch festhalten.</div>
    <div class="photo tone-grey" style="left:120px;top:0;width:40px;height:20px" role="img" aria-label="Familie mit Baby"></div>
    <div class="card tiny" style="left:120px;top:20px;width:40px;height:40px;padding:3px"><b style="color:var(--red)">Fotostudio Jonas Keller</b></div>
    <div class="photo tone-blue" style="left:120px;top:60px;width:40px;height:20px" role="img" aria-label="Baby im Korb"></div>
  </section>

  <section class="spread row2" aria-label="Innenseite">
    <div class="photo tone-park" style="left:0;top:0;width:133px;height:67px" role="img" aria-label="Schwangere Frau im Park"></div>
    <div class="photo tone-dark" style="left:0;top:67px;width:133px;height:133px" role="img" aria-label="Schwangere Frau mit kleinem Sohn vor dunklem Hintergrund"></div>
    <div class="photo tone-warm" style="left:0;top:200px;width:133px;height:66px" role="img" aria-label="Neugeborenes mit Bärenmütze"></div>

    <h2 class="script abs" style="left:133px;top:8px;width:266px;text-align:center;font-weight:400;font-size:22px;line-height:1.25">… wie die ersten<br>Lebenstage eures Babys!</h2>
    <div class="photo tone-soft" style="left:144px;top:68px;width:122px;height:75px;transform:rotate(-2deg)" role="img" aria-label="Neugeborenes auf heller Decke"></div>
    <div class="photo tone-field" style="left:266px;top:66px;width:120px;height:75px;transform:rotate(2deg)" role="img" aria-label="Werdende Eltern liegen auf einer Wiese"></div>
    <div class="card body-text" style="left:146px;top:146px;width:240px;height:120px;padding:14px 12px 0 11px">
      <p>Das letzte Drittel der Schwangerschaft, eine spannende Zeit. Der Babybauch wird immer größer, runder und die Freude, Euer Baby in den Händen zu halten wächst jeden Tag.</p>
      <p style="margin-top:5px">Als Fotograf bin ich auf die <b>Schwangerschaft- und Neugeborenenfotografie</b> spezialisiert und halte Euch diese so wertvollen Momente für immer fest.</p>
    </div>

    <div class="photo tone-grey" style="left:399px;top:0;width:133px;height:67px" role="img" aria-label="Eltern mit Neugeborenem in Schwarzweiß"></div>
    <div class="card" style="left:399px;top:67px;width:133px;height:133px;padding:27px 0 0 13px">
      <p class="contact-title">Fotostudio<br>Jonas Keller</p>
      <ul class="contact-list">
        <li><svg viewBox="0 0 10 10"><path d="M5 0a3.5 3.5 0 0 0-3.5 3.5C1.5 6 5 10 5 10s3.5-4 3.5-6.5A3.5 3.5 0 0 0 5 0zm0 5a1.5 1.5 0 1 1 0-3 1.5 1.5 0 0 1 0 3z"/></svg><span>Lindenweg 9<br>72100 Talbach</span></li>
        <li><svg viewBox="0 0 10 10"><path d="M2 0l2 2.3-1 1.4a6 6 0 0 0 3.3 3.3l1.4-1L10 8l-1.3 1.6C4.5 10 0 5.5.4 1.3z"/></svg><span>(0 71 23) 45 67 890</span></li>
        <li><svg viewBox="0 0 10 10"><path d="M0 2h10v6H0zM0 2l5 3.5L10 2" stroke="#fff" stroke-width=".8"/></svg><span>jonas@babyfotos-kellerstudio.de</span></li>
        <li><svg viewBox="0 0 10 10"><rect x=".5" y="1" width="9" height="7" fill="none" stroke="#8e2a1f"/><path d="M2 3h6v1H2z"/></svg><span>www.babyfotos-kellerstudio.de</span></li>
        <li><svg viewBox="0 0 10 10"><rect width="10" height="10" rx="1"/></svg><span>kellerstudio.babyfotos</span></li>
      </ul>
    </div>
    <div class="photo tone-blue" style="left:399px;top:200px;width:133px;height:66px" role="img" aria-label="Neugeborenes schlafend im Korb"></div>
  </section>

  <!-- Bildseite mit Beschnittzonen -->
  <section class="thumb row3" aria-label="Vorschau Bildseite mit Beschnittzonen" style="background:var(--white)">
    <div class="abs" style="left:0;top:0;width:40px;height:80px">
      <div class="band" style="top:0;height:20px;background:var(--band-red)">Bereich nicht gestalten</div>
      <div class="band" style="top:20px;height:40px;background:var(--band-orange)">Bereich vom Knick übernommen</div>
      <div class="band" style="top:60px;height:20px;background:var(--band-red)">Bereich nicht gestalten</div>
    </div>
    <div class="photo tone-warm" style="left:41px;top:1px;width:38px;height:39px" role="img" aria-label="Neugeborenes"></div>
    <div class="photo tone-soft" style="left:81px;top:1px;width:38px;height:38px" role="img" aria-label="Babyfüße"></div>
    <div class="photo tone-blue" style="left:41px;top:41px;width:38px;height:38px" role="img" aria-label="Baby im Korb"></div>
    <div class="photo tone-dark" style="left:81px;top:40px;width:38px;height:39px" role="img" aria-label="Paar mit Babybauch"></div>
    <div class="brand" style="left:68px;top:28px;width:24px;height:24px"><span class="brand-name" style="font-size:2px">Jonas Keller</span></div>
    <div class="abs" style="left:120px;top:0;width:40px;height:80px">
      <div class="band" style="top:0;height:20px;background:var(--band-red)">Bereich nicht gestalten</div>
      <div class="band" style="top:20px;height:40px;background:var(--band-orange)">Bereich vom Knick übernommen</div>
      <div class="band" style="top:60px;height:20px;background:var(--band-red)">Bereich nicht gestalten</div>
    </div>
  </section>

  <section class="spread row3" aria-label="Bildseite" style="background:var(--white)">
    <div class="abs" style="left:133px;top:0;width:266px;height:266px;background:var(--beige-light)"></div>
    <div class="photo tone-warm" style="left:134px;top:2px;width:128px;height:155px;transform:rotate(-1.5deg)" role="img" aria-label="Neugeborenes schlafend, Kopf auf den Händen"></div>
    <div class="photo tone-soft" style="left:270px;top:3px;width:128px;height:100px;transform:rotate(2deg)" role="img" aria-label="Babyfüße in heller Wolle"></div>
    <div class="photo tone-blue" style="left:135px;top:158px;width:128px;height:104px;transform:rotate(1.5deg)" role="img" aria-label="Neugeborenes im Korb auf Jute"></div>
    <div class="photo tone-dark" style="left:268px;top:108px;width:130px;height:156px;transform:rotate(-2deg)" role="img" aria-label="Paar mit Babybauch vor dunklem Hintergrund"></div>
    <div class="brand" style="left:224px;top:89px;width:84px;height:84px">
      <span class="brand-name" style="font-size:4.4px">Jonas Keller<br><span style="text-transform:none;letter-spacing:.08em;font-size:3.6px">babyfotos-kellerstudio.de</span></span>
    </div>
  </section>

  <!-- Gründe -->
  <section class="thumb row4" aria-label="Vorschau Gründeseite">
    <div class="card tiny" style="left:3px;top:3px;width:36px;height:74px;padding:2px">Kurze Gründe für Euer Shooting</div>
    <div class="script abs" style="left:42px;top:4px;width:76px;text-align:center;font-size:6px">31 gute Gründe für<br>ein Shooting bei mir…</div>
    <div class="card tiny" style="left:46px;top:22px;width:68px;height:55px;padding:2px">Kurze Gründe für Euer Shooting</div>
    <div class="card tiny" style="left:121px;top:3px;width:36px;height:74px;padding:2px">Kurze Gründe für Euer Shooting</div>
  </section>

  <section class="spread row4" aria-label="31 gute Gründe">
    <div class="card reasons" style="left:14px;top:10px;width:108px;height:248px;padding:5px 3px 0 2px">
      <p><span class="key">1. Fotos als Datei:</span> Im Shooting sind immer Fotos als digitale Datei enthalten.</p>
      <p><span class="key">2. Erfahrung:</span> Seit 2010 habe ich mich auf die Fotografie von Schwangeren &amp; Neugeborenen spezialisiert.</p>
      <p><span class="key">3. Parkplatz am Studio</span></p>
      <p><span class="key">4. Spielekiste für die „Großen“:</span> Spiele, Bücher,… für das Geschwisterkind.</p>
      <p><span class="key">5. Sicherheit ist das A&amp;O:</span> Euer Baby wird nur in Posen fotografiert, die auch sicher sind.</p>
      <p><span class="key">6. Windeln &amp; Hygieneprodukte:</span> Spart Euch das schleppen, im Studio steht alles für Euch zur Verfügung.</p>
      <p><span class="key">7. Kostenloses WLAN</span></p>
      <p><span class="key">8. Requisitenauswahl:</span> Tücher, Decken, Mützchen, Haarbänder, Körbchen und vieles mehr stehen zur Verfügung.</p>
      <p><span class="key">9. Bequeme Fotoauswahl Zuhause:</span> Zuhause über eine kennortgeschützte Onlinegalerie könnt ihr Eure Fotos anschauen.</p>
      <p><span class="key">10. Gemütlicher Stillbereich</span></p>
    </div>

    <h2 class="script abs" style="left:133px;top:10px;width:266px;text-align:center;font-weight:400;font-size:22px;line-height:1.28">31 gute Gründe für<br>ein Shooting bei mir…</h2>
    <div class="card reasons" style="left:146px;top:70px;width:240px;height:188px;padding:6px 6px 0 5px;display:flex;gap:9px">
      <div style="flex:1">
        <p><span class="key">11. Babybauchkleider:</span> Im Fundus ist sicherlich auch für Dich was passendes dabei.</p>
        <p><span class="key">12. Spezialisiert:</span> Auf Schwangere, Neugeborene, Babys und Familien - Euer Familienfotograf.</p>
        <p><span class="key">13. Individuelle Shootings:</span> jedes Shooting auf Eure Wünsche und Vorstellungen angepasst.</p>
        <p><span class="key">14. Flexibel:</span> Babybauch &amp; Familienshootings auch an Eurem Wunschort</p>
        <p><span class="key">15. Kurze Bearbeitungszeiten:</span> Innerhalb von 5 Werktagen erhaltet ihr die Galerie mit Euren Fotos fix &amp; fertig retuschiert zum anschauen.</p>
        <p><span class="key">16. Sofort verfügbare Bilder:</span> Ausgewählte Bilder stehen nach Bestellung &amp; Zahlung sofort als Download zur Verfügung.</p>
      </div>
      <div style="flex:1">
        <p><span class="key">17. Erste-Hilfe:</span> Ich frische mein Wissen in Erste-Hilfe regelmäßig auf, speziell für den Kleinkind und Säuglingsbereich.</p>
        <p><span class="key">18. Autobahnnah:</span> Nur 15 Minuten von der Autobahnausfahrt Talheim Ost entfernt.</p>
        <p><span class="key">19. Angebote:</span> Durch regelmäßige Aktionen könnt ihr Geld sparen.</p>
        <p><span class="key">20. Diskretion:</span> Freigaben und Veröffentlichungen werden immer vorher abgesprochen.</p>
        <p><span class="key">21. 100% Ausführung:</span> auch im Krankheitsfall, durch ein Netzwerk an Kollegen.</p>
        <p><span class="key">22. Referenzen:</span> Viele Babybäuche, Babys und Familien durfte ich bereits fotografieren.</p>
        <p><span class="key">23. Geduld:</span> Ich nehme mir die Zeit und Geduld die Euer Baby braucht.</p>
      </div>
    </div>

    <div class="card reasons" style="left:410px;top:10px;width:112px;height:248px;padding:5px 3px 0 5px">
      <p><span class="key">24. Regelmäßig neue Fotos:</span> Mit dem Babypass begleite ich Euch vom Babybauch, über die Neugeborenenfotos bis zum 3. Lebensjahr Eures Kindes.</p>
      <p><span class="key">25. Abendshooting:</span> Natürlich kann das Babybauchshooting auch am Abend statt finden, wenn der Papa Feierabend hat.</p>
      <p><span class="key">26. Zufriedenheit:</span> Sollte Euer Kind mal keine Lust haben auf das Shooting, verschieben wir den Termin und vereinbaren einen neuen.</p>
      <p><span class="key">27. Empfehlungen:</span> Ihr benötigt Geburtskarten oder Wandbilder, gerne geben wir hier eine Empfehlung.</p>
      <p><span class="key">28. Immer aktuell:</span> Das Equipement wird regelmäßig gewartet und neue Requisiten sorgen für Abwechslung.</p>
      <p><span class="key">29. EC Zahlung</span></p>
      <p><span class="key">30. Hochwertige Produkte:</span> Bei den verwendeten Requisiten und Produkten wird viel Wert auf natürliche und hochwertige Produkte gelegt.</p>
      <p><span class="key">31. Getränke:</span> Kaffee, Tee und Mineralwasser stehen im Studio für Euch bereit.</p>
    </div>
  </section>

</main>
</body>
</html>
```